Company Values - print for wall

We ned a print of our values on one of the walls in our office. Create a couple of suggestions that we can print on our walls.

Summary:
- See power point with values
- make two suggestion: one with only titles + one with titles and bulletpoints / use the "We" version)
- make a suggestion in a moon raiders theme
- see brand book for inspiration
- see images of office for inspiration
Updates

The company's values that we want to highlight are: 1. Exceed expectations 2. Execute with passion 3. Empower each other Exceed expectations:​ • We establish a good understanding of current expectations.​ • We provide helpful, honest, and timely feedback.​ • We deliver impressive quality.​ Execute with passion:​ • We embrace change.​ • We seek innovative solutions.​ • We inspire others with your actions and attitudes. ​ • We care about success. ​ • We are confident and humble. Empower each other:​ • We are available to help colleagues.​ • We are open-minded.​ • We seek and share information proactively.​ • We respect others’ time.​ This is in line with achieving the company vision: « Our vision is to make a difference for our customers through our highly customizable solutions for planning, execution, and analysis. It’s less about the software itself and more about customer success. Make better decisions faster with Clearmont. »​ Eirik Tove Malmberg, CEO Clearmont Company slogan: Better Decisions Faster​ It's a lot of text above, but what we what to emphasize most are the following text above and here again: exceed expectations, execute with passion, empower each other We can do something fun and cool with the Moon Raiders theme as this is internal - that's the visual that would work with the company culture.

Font styles to use
Sans Serif

Requirements
Nice to have
• - one suggestion with Montserrat font
- one suggestion in moon raiders font

```html
<!DOCTYPE html>
<html lang="en">
<head>
<meta charset="utf-8">
<title>Values – Wall Print</title>
<link rel="stylesheet" href="https://fonts.googleapis.com/css2?family=Audiowide&family=Montserrat:wght@400;500&display=swap">
<style>
  :root {
    --backdrop: #1f1d1d;
    --rim-light: #e6e6e6;
    --rim-dark: #8a8a8a;
    --space-black: #07090d;
    --ocean-blue: #1c6fd0;
    --cloud-grey: #8c9bb0;
    --accent-cyan: #4fc6f5;
    --accent-blue: #1d8fe0;
    --text-white: #ffffff;
  }
  * { margin: 0; padding: 0; box-sizing: border-box; }
  html, body {
    width: 1200px; height: 1200px; overflow: hidden;
    background: var(--backdrop);
  }
  .canvas { position: relative; width: 1200px; height: 1200px; }
  .rim {
    position: absolute; left: 109px; top: 109px; width: 982px; height: 982px;
    border-radius: 50%;
    background: linear-gradient(160deg, var(--rim-dark) 0%, var(--rim-light) 35%, #f4f4f4 55%, var(--rim-dark) 100%);
  }
  .globe {
    position: absolute; left: 133px; top: 133px; width: 934px; height: 934px;
    border-radius: 50%; overflow: hidden;
    background:
      radial-gradient(circle at 30% 22%, rgba(170,185,205,0.75) 0%, rgba(110,130,160,0.45) 22%, transparent 48%),
      radial-gradient(circle at 35% 40%, var(--ocean-blue) 0%, #0f3f80 35%, var(--space-black) 68%);
  }
  .panel { position: absolute; inset: 0; text-align: center; color: var(--text-white); }
  .title {
    position: absolute; top: 248px; left: 0; width: 100%;
    font-family: "Audiowide", sans-serif; font-size: 68px; letter-spacing: 1px;
    color: var(--text-white); text-shadow: 0 8px 0 #000;
  }
  .value-heading {
    position: absolute; left: 0; width: 100%;
    display: flex; align-items: center; justify-content: center; gap: 14px;
    font-family: "Audiowide", sans-serif; font-size: 27px; text-transform: uppercase;
    color: var(--accent-cyan);
  }
  .value-heading span {
    background: linear-gradient(180deg, var(--accent-cyan), var(--accent-blue));
    -webkit-background-clip: text; background-clip: text; color: transparent;
  }
  .rule {
    width: 98px; height: 8px; border: 1.5px solid var(--accent-cyan); border-radius: 4px;
    background: rgba(29,143,224,0.35);
  }
  .value-points {
    position: absolute; left: 0; width: 100%; list-style: none;
    font-family: "Montserrat", sans-serif; font-weight: 500; font-size: 19.5px; line-height: 28px;
  }
  .h1 { top: 377px; } .p1 { top: 419px; }
  .h2 { top: 560px; } .p2 { top: 603px; }
  .h3 { top: 794px; } .p3 { top: 837px; }
</style>
</head>
<body>
<div class="canvas">
  <div class="rim"></div>
  <div class="globe" role="img" aria-label="Photograph of planet Earth seen from space, clouds over blue oceans and glowing city lights on the night side"></div>
  <div class="panel">
    <h1 class="title">VALUES</h1>

    <h2 class="value-heading h1"><i class="rule"></i><span>Exceed Expectations:</span><i class="rule"></i></h2>
    <ul class="value-points p1">
      <li>We establish a good understanding of current expectations.</li>
      <li>We provide helpful, honest, and timely feedback.</li>
      <li>We deliver impressive quality.</li>
    </ul>

    <h2 class="value-heading h2"><i class="rule"></i><span>Execute with Passion:</span><i class="rule"></i></h2>
    <ul class="value-points p2">
      <li>We embrace change.</li>
      <li>We seek innovative solutions.</li>
      <li>We inspire others with your actions and attitudes.</li>
      <li>We care about success.</li>
      <li>We are confident and humble.</li>
    </ul>

    <h2 class="value-heading h3"><i class="rule"></i><span>Empower Each Other:</span><i class="rule"></i></h2>
    <ul class="value-points p3">
      <li>We are available to help colleagues.</li>
      <li>We are open-minded.</li>
      <li>We seek and share information proactively.</li>
      <li>We respect others’ time.</li>
    </ul>
  </div>
</div>
</body>
</html>
```